Tallbrook Sonic Group, Inc.
Project: Business Cards
Business Cards  - Health
Business Cards
Professional
2 Versions: Person 1. Marla Pennington, BSBA, BSDMS, RDMS Person 2. Gavin Pennington
Person 1. [no title] Person 2. Vice President, Sales
Ultrasound Services Sonographer Staffing PACS / Reporting
info@tallbrooksg.com
www.tallbrooksg.com
Member: CVRTB, NLUA & PSEK
Would prefer light color(s) or white background to match logo - no black backgrounds please. Let me know if you have any questions. Thanks!

```html
<!DOCTYPE html>
<html lang="en">
<head>
<meta charset="utf-8">
<title>Tallbrook Sonic Group, Inc. — Business Cards</title>
<link href="https://fonts.googleapis.com/css2?family=Mulish:wght@400;600&display=swap" rel="stylesheet">
<style>
  :root {
    --backdrop: #4a4037;
    --card: #ffffff;
    --teal: #1d5a6c;
    --teal-light: #2f7488;
    --slate: #5c6770;
    --ink: #3f4a52;
    --mark: #3c6f80;
  }
  * { box-sizing: border-box; margin: 0; padding: 0; }
  html, body { width: 1200px; height: 904px; overflow: hidden; }
  body {
    background: var(--backdrop);
    font-family: "Mulish", sans-serif;
    position: relative;
  }
  .card {
    position: absolute;
    width: 620px;
    height: 354px;
    background: var(--card);
    box-shadow: 0 10px 28px rgba(0,0,0,0.45);
    overflow: hidden;
  }
  .card--front { left: 70px; top: 80px; }
  .card--back { left: 510px; top: 470px; }

  .brand {
    display: flex;
    align-items: center;
    gap: 12px;
    color: var(--mark);
    font-weight: 600;
    letter-spacing: 0.04em;
  }
  .brand__dot {
    width: 28px; height: 28px;
    border-radius: 50%;
    background: var(--mark);
    flex: none;
  }
  .card--front .brand {
    position: absolute;
    left: 0; right: 0; top: 160px;
    justify-content: center;
    font-size: 22px;
  }
  .card--back .brand {
    position: absolute;
    left: 34px; top: 62px;
    font-size: 17px;
  }
  .card--back .brand__dot { width: 22px; height: 22px; }

  .person {
    position: absolute;
    right: 34px; top: 92px;
    text-align: left;
    color: var(--ink);
  }
  .person__name { font-size: 17px; font-weight: 600; color: var(--teal); }
  .person__creds { font-size: 12px; margin-top: 4px; letter-spacing: 0.03em; }

  .bands { position: absolute; left: 0; top: 0; }

  .website {
    position: absolute;
    right: 22px; top: 232px;
    color: #fff;
    font-size: 12px;
    letter-spacing: 0.12em;
  }

  .details {
    position: absolute;
    left: 34px; top: 232px;
    color: var(--slate);
    font-size: 11.5px;
    line-height: 1.45;
  }
  .details__row { display: flex; align-items: center; gap: 6px; }
  .details__icon { width: 11px; height: 11px; flex: none; }
</style>
</head>
<body>

  <section class="card card--front" aria-label="Card front">
    <div class="brand">
      <span class="brand__dot"></span>
      <span class="brand__name">Tallbrook Sonic Group, Inc.</span>
    </div>
  </section>

  <section class="card card--back" aria-label="Card back">
    <svg class="bands" width="620" height="354" viewBox="0 0 620 354" aria-hidden="true">
      <polygon points="300,226 620,226 620,256 270,256" fill="var(--teal)"/>
      <polygon points="0,322 240,322 258,304 620,304 620,312 262,312 246,328 0,328" fill="var(--slate)"/>
      <polygon points="0,336 250,336 268,318 620,318 620,354 0,354" fill="var(--teal)"/>
      <polygon points="248,336 266,318 300,318 282,336" fill="var(--teal-light)"/>
    </svg>

    <div class="brand">
      <span class="brand__dot"></span>
      <span class="brand__name">Tallbrook Sonic Group, Inc.</span>
    </div>

    <div class="person">
      <p class="person__name">Marla Pennington</p>
      <p class="person__creds">BSBA, BSDMS, RDMS</p>
    </div>

    <p class="website">www.tallbrooksg.com</p>

    <div class="details">
      <p>Ultrasound Services</p>
      <p>Sonographer Staffing</p>
      <p>PACS / Reporting</p>
      <p class="details__row">
        <svg class="details__icon" viewBox="0 0 12 12" aria-hidden="true"><path d="M2.5 1 L4.5 1 L5.2 3.6 L4 4.6 C4.7 6 6 7.3 7.4 8 L8.4 6.8 L11 7.5 L11 9.5 C11 10.3 10.3 11 9.5 11 C5 11 1 7 1 2.5 C1 1.7 1.7 1 2.5 1 Z" fill="var(--slate)"/></svg>
        (555) 214-0187
      </p>
      <p class="details__row">
        <svg class="details__icon" viewBox="0 0 12 12" aria-hidden="true"><rect x="0.5" y="2" width="11" height="8" fill="var(--slate)"/><path d="M0.5 2 L6 6.5 L11.5 2" fill="none" stroke="#fff" stroke-width="1"/></svg>
        info@tallbrooksg.com
      </p>
    </div>
  </section>

</body>
</html>
```